Sydney law firm, Prestwicks Solicitors, needs a flyer design!

We need a flyer design for our law firm which has been operating in Sydney for over 35 years. We want to send the flyer out to potential clients and also to existing clients to let them know the range of services that we provide. Our corporate colours are white, red and black and we would like these incorporated somewhat. The final design should be clean, modern and professional.

We would like the design to fit a double sided flyer approx. 210mm high x 100mm wide.

Industry/Entity Type

Law Firm

Font styles to use
Serif
Sans Serif

Colors
eb2026
ffffff

Requirements
Must have
• Details needed on the flyer are:
• Prestwicks Solicitors
• 3/82 Carradine Street, Liverpool, NSW 2170
• (02) 9418 3562
• www.prestwickssolicitors-example.com.au
• info@prestwickssolicitors-example.com.au
• Our areas of practice include:
• Property Law
• Conveyancing
• Leases
• Criminal Law
• Family Law
• Litigation and Dispute Resolution
• Company Law
• Wills and Estates
• Powers of Attorney and Guardianship
Should not have
• a picture of scales or a picture of a gavel

```html
<!DOCTYPE html>
<html lang="en">
<head>
<meta charset="utf-8">
<title>Prestwicks Solicitors – Flyer</title>
<link href="https://fonts.googleapis.com/css2?family=Open+Sans:wght@400;600;700&display=swap" rel="stylesheet">
<style>
  :root {
    --brand-red: #eb2026;
    --brand-red-deep: #d11a20;
    --ink: #3a3a3a;
    --ink-soft: #555555;
    --paper: #ffffff;
    --backdrop: #e9e9e9;
    --photo-dark: #1c1c1c;
    --photo-mid: #7a7a7a;
    --photo-light: #d6d6d6;
  }
  * { box-sizing: border-box; margin: 0; padding: 0; }
  html, body { width: 1200px; height: 800px; overflow: hidden; }
  body {
    background: var(--backdrop);
    font-family: "Open Sans", Arial, sans-serif;
    position: relative;
  }
  .flyer {
    position: absolute;
    left: 280px;
    top: 20px;
    width: 640px;
    height: 760px;
    background: var(--paper);
    box-shadow: 0 2px 10px rgba(0,0,0,0.18);
    overflow: hidden;
  }
  .flyer__photo {
    position: absolute;
    left: 0; top: 0;
    width: 640px; height: 380px;
    background:
      radial-gradient(ellipse 70% 45% at 55% 62%, var(--photo-light) 0%, var(--photo-mid) 55%, transparent 80%),
      linear-gradient(180deg, var(--photo-dark) 0%, #2e2e2e 40%, #8c8c8c 75%, #b8b8b8 100%);
  }
  .intro {
    position: absolute;
    left: 22px; top: 412px;
    width: 285px;
    color: var(--ink-soft);
    font-size: 12.5px;
    line-height: 1.3;
  }
  .intro p + p { margin-top: 14px; }
  .firm-name {
    position: absolute;
    left: 22px; top: 575px;
    font-size: 23px;
    font-weight: 600;
    color: var(--ink);
    letter-spacing: 0.5px;
  }
  .contact {
    position: absolute;
    left: 22px; top: 618px;
    list-style: none;
    color: var(--brand-red);
    font-size: 12px;
    line-height: 1.35;
  }
  .website {
    position: absolute;
    left: 22px; top: 700px;
    color: var(--brand-red);
    font-size: 12px;
    font-weight: 700;
  }
  .services {
    position: absolute;
    left: 322px; top: 345px;
    width: 283px; height: 383px;
    background: linear-gradient(180deg, var(--brand-red-deep), var(--brand-red));
    border-radius: 16px;
    list-style: none;
    display: flex;
    flex-direction: column;
    justify-content: center;
    align-items: center;
    text-align: center;
    color: var(--paper);
    font-size: 16.5px;
    line-height: 1.1;
    padding: 10px 14px;
  }
  .services__item + .services__item::before {
    content: "•";
    display: block;
    font-size: 9px;
    line-height: 1;
    margin: 4px 0 3px;
  }
</style>
</head>
<body>
  <article class="flyer">
    <div class="flyer__photo" role="img" aria-label="Black and white photograph of rolled newspapers lined up on a table"></div>

    <section class="intro">
      <p>Prestwicks Solicitors is a private law firm based in Liverpool that has been servicing the Sydney area for over 30 years. With a dedicated, professional and friendly team we pride ourselves on delivering an exceptional legal service to our clients.</p>
      <p>Offering a complete legal service at affordable rates, our clients really do come first.</p>
    </section>

    <div class="firm-name">Prestwicks Solicitors</div>

    <ul class="contact">
      <li>3/82 Carradine Street, Liverpool, NSW 2170</li>
      <li>(02) 9418 3562</li>
      <li>info@prestwickssolicitors-example.com.au</li>
    </ul>

    <div class="website">www.prestwickssolicitors-example.com.au</div>

    <ul class="services">
      <li class="services__item">Property Law</li>
      <li class="services__item">Conveyancing</li>
      <li class="services__item">Leases</li>
      <li class="services__item">Criminal Law</li>
      <li class="services__item">Family Law</li>
      <li class="services__item">Litigation and<br>Dispute Resolution</li>
      <li class="services__item">Company Law</li>
      <li class="services__item">Wills and Estates</li>
      <li class="services__item">Powers of Attorney and<br>Guardianship</li>
    </ul>
  </article>
</body>
</html>
```